Packing for a Vodka Fruit Mix Drink wanted!

We are looking for a modern and elegant design for the packaging of a Vodka Fruit Mix Drink. The drink is filled into a 100ml (90 x 145 mm) SpoutBag (Veltrisa) and shoulderstand be sold in different varieties. The packaging shoulderstand be very plain, simple and modern. Less is more! The logo Should be Placed large and centrally. The background shoulderstand be dark. - But if a bright background is more effective, You Could convince us. In addition, the types of fruit and vodka shoulderstand be read. (Eg Mango - Pineapple - Vodka) There will be in the future, different varieties, there Should be a color scheme for the various varieties. Each variety shoulderstand be Recognized equal to the shelf. (For example, lines of different colors, denominations, ...) Font: http://www.glyphmarket-example.com/search.html?search=tornelle&x=0&y=0
Reason: I am on holiday till 18. May

```html
<!DOCTYPE html>
<html lang="de">
<head>
<meta charset="utf-8">
<title>Corvina Fresh – Mango Pineapple Vodka Label</title>
<link rel="stylesheet" href="https://fonts.googleapis.com/css2?family=Michroma&family=Fira+Sans:wght@400;500&display=swap">
<style>
  :root {
    --stage: #5b3d24;
    --label-center: #f6f300;
    --label-mid: #e2e000;
    --label-edge: #b3af00;
    --ink: #111100;
    --accent: #e3101a;
    --fruit-dark: #1c1b08;
    --fruit-mid: #5f5d10;
  }
  html, body {
    margin: 0;
    padding: 0;
    width: 1200px;
    height: 907px;
    overflow: hidden;
    background: var(--stage);
  }
  .canvas {
    position: relative;
    width: 1200px;
    height: 907px;
    background: var(--stage);
    color: var(--ink);
  }
  .label {
    position: absolute;
    overflow: hidden;
    box-shadow: 0 4px 14px rgba(0,0,0,.35);
  }
  .label--front {
    left: 82px; top: 55px; width: 496px; height: 800px;
    background: radial-gradient(ellipse 70% 55% at 50% 46%, var(--label-center) 0%, var(--label-mid) 45%, var(--label-edge) 100%);
  }
  .label--back {
    left: 625px; top: 55px; width: 495px; height: 798px;
    background: radial-gradient(ellipse 75% 60% at 50% 40%, var(--label-center) 0%, var(--label-mid) 50%, var(--label-edge) 100%);
  }
  .brand-mark {
    position: absolute;
    border-radius: 50%;
    background: var(--accent);
  }
  .label--front .brand-mark { left: 180px; top: 275px; width: 120px; height: 120px; }
  .label--back .brand-mark { left: 215px; top: 35px; width: 58px; height: 58px; }
  .brand-name {
    position: absolute;
    left: 0; right: 0;
    text-align: center;
    font-family: "Michroma", sans-serif;
    font-weight: 400;
    color: var(--ink);
    margin: 0;
    line-height: 1;
  }
  .label--front .brand-name {
    top: 418px;
    font-size: 21px;
    letter-spacing: 1px;
  }
  .variety {
    position: absolute;
    top: 451px; left: 0; right: 0;
    text-align: center;
    font-family: "Michroma", sans-serif;
    font-size: 15px;
    line-height: 1;
    letter-spacing: 7px;
    margin: 0;
  }
  .fruit-art {
    position: absolute;
    left: 306px; top: 593px;
    width: 190px; height: 207px;
    background: linear-gradient(160deg, var(--fruit-mid) 0%, var(--fruit-dark) 100%);
  }
  .label--back .brand-name {
    top: 114px;
    font-size: 12px;
    letter-spacing: 1px;
  }
  .section-title {
    font-family: "Michroma", sans-serif;
    font-size: 13px;
    letter-spacing: 5px;
    text-decoration: underline;
    text-underline-offset: 3px;
    text-align: center;
    margin: 0;
  }
  .section-text {
    font-family: "Fira Sans", sans-serif;
    font-size: 12.5px;
    line-height: 15.5px;
    text-align: center;
    margin: 0;
  }
  .ingredients-de { position: absolute; top: 161px; left: 0; right: 0; }
  .ingredients-en { position: absolute; top: 277px; left: 0; right: 0; }
  .ingredients-de .section-text,
  .ingredients-en .section-text { margin-top: 13px; padding: 0 62px; }
  .nutrition {
    position: absolute;
    left: 28px; top: 379px;
    width: 437px;
    border-collapse: collapse;
    font-family: "Fira Sans", sans-serif;
    font-size: 12.5px;
  }
  .nutrition th, .nutrition td {
    border: 1.5px solid var(--ink);
    padding: 0 10px;
    height: 20px;
    text-align: left;
    font-weight: 400;
  }
  .nutrition th {
    font-family: "Michroma", sans-serif;
    font-size: 11.5px;
    height: 22px;
  }
  .nutrition td:first-child, .nutrition th:first-child { width: 239px; }
  .producer { position: absolute; top: 630px; left: 0; right: 0; }
  .producer .section-text { margin-top: 10px; line-height: 16px; }
  .tagline {
    position: absolute;
    top: 754px; left: 0; right: 0;
    text-align: center;
    font-family: "Michroma", sans-serif;
    font-size: 16px;
    line-height: 1;
    letter-spacing: 7px;
    margin: 0;
  }
</style>
</head>
<body>
<div class="canvas">
  <section class="label label--front">
    <div class="brand-mark" aria-hidden="true"></div>
    <h1 class="brand-name">CORVINA FRESH</h1>
    <p class="variety">Mango - Pineapple - Vodka</p>
    <div class="fruit-art" role="img" aria-label="Stylised fruit illustration: stacked round fruits drawn as concentric rings with a leaf on top"></div>
  </section>

  <section class="label label--back">
    <div class="brand-mark" aria-hidden="true"></div>
    <h2 class="brand-name">CORVINA FRESH</h2>

    <div class="ingredients-de">
      <h3 class="section-title">Smoothie mit Vodka:</h3>
      <p class="section-text">Zutaten: Apfel 40%, Mango 20%, Ananas 20%, Vodka 20%,<br>Pasteurisiert, Mindestens haltbar bis: siehe Aufdruck unten.<br>Nach dem Öffnen gekühlt lagern und innerhalb von wenigen<br>Tagen verzehren.</p>
    </div>

    <div class="ingredients-en">
      <h3 class="section-title">Smoothie with Vodka:</h3>
      <p class="section-text">Ingredients: Apple 40%, 20% mango, pineapple 20%, vodka 20%,<br>pasteurized, Best before: see imprint below. Store cooled<br>after opening and consume within a few days.</p>
    </div>

    <table class="nutrition">
      <tr><th>Nährwerte pro</th><th>100g</th></tr>
      <tr><td>Brennwert:</td><td>330kJ / 78kcal</td></tr>
      <tr><td>Fett:</td><td>0,5g</td></tr>
      <tr><td>davongesättigteFettsäuren:</td><td>0,1g</td></tr>
      <tr><td>Kohlenhydrate:</td><td>17g</td></tr>
      <tr><td>davonZucker:</td><td>16g</td></tr>
      <tr><td>Alkohol:</td><td>9g</td></tr>
      <tr><td>Eiweiß:</td><td>&lt;0,5g</td></tr>
      <tr><td>Salz:</td><td>&lt;0,01g</td></tr>
      <tr><td>Vitamin C</td><td>13,4g</td></tr>
    </table>

    <div class="producer">
      <h3 class="section-title">Hersteller:</h3>
      <p class="section-text">Corvina Fresh GmbH<br>Lindenweg 8<br>5120 Almbach<br>www.corvina-fresh.at</p>
    </div>

    <p class="tagline">Shake it - Drink it</p>
  </section>
</div>
</body>
</html>
```